Business Card for Inovative Flexible Packaging Company

Create a business card that is both simple and stricking at the same time.
Preferably only one color (orange) or two colors (black and orange).
Information to print:
Torvalo, Lda
[T] 22 418 6093
[M] 91 326 7041
[F] 22 418 6135
[@] torvalo.ac@correiomx.com
SEDE & ARMAZÉM
Rua Das Figueiras do Monte, 312
Valmora
4520-832 Valmora - VN Teixal
PORTUGAL
Reason: A lot of the ideas are obvious. I want something different. Inovative. dare to do something eye catching with style.
Business Consumers. Packaging Designers.
Business

```html
<!DOCTYPE html>
<html lang="pt">
<head>
<meta charset="utf-8">
<title>Torvalo, Lda — Business Card</title>
<link href="https://fonts.googleapis.com/css2?family=Open+Sans:wght@400;600;700&display=swap" rel="stylesheet">
<style>
  :root {
    --orange: #e8720c;
    --orange-light: #f08a1c;
    --ink: #3a3a3a;
    --ink-soft: #6b6b6b;
    --card: #f4f4f2;
    --backdrop: #d9d9d6;
  }
  * { box-sizing: border-box; margin: 0; padding: 0; }
  html, body {
    width: 1200px; height: 900px; overflow: hidden;
    background: var(--backdrop);
    font-family: "Open Sans", Arial, sans-serif;
    color: var(--ink);
  }
  .canvas {
    position: relative; width: 1200px; height: 900px;
    display: flex; align-items: center; justify-content: center; gap: 40px;
  }
  .card {
    position: relative; width: 540px; height: 315px;
    background: var(--card);
    box-shadow: 0 6px 18px rgba(0,0,0,.12);
    overflow: hidden;
  }
  .brand-name {
    font-weight: 700; color: var(--orange);
    line-height: 1; letter-spacing: -1px;
  }
  .brand-tagline {
    font-size: 9px; letter-spacing: 4.2px; text-transform: uppercase;
    color: var(--ink-soft); font-weight: 600; white-space: nowrap;
  }

  /* Front */
  .card--front .brand-mark {
    position: absolute; left: 0; top: 60px;
    width: 195px; height: 195px;
    background: linear-gradient(135deg, var(--orange-light), var(--orange));
  }
  .card--front .brand {
    position: absolute; right: 36px; top: 44px; text-align: right;
  }
  .card--front .brand-name { font-size: 46px; }
  .card--front .brand-tagline { margin-top: 4px; font-size: 8px; letter-spacing: 3.6px; }

  /* Back */
  .card--back .brand {
    position: absolute; left: 40px; top: 44px;
    display: flex; align-items: flex-start; gap: 16px;
  }
  .card--back .brand-mark {
    width: 72px; height: 72px; margin-top: 8px;
    background: linear-gradient(135deg, var(--orange-light), var(--orange));
  }
  .card--back .brand-name { font-size: 60px; }
  .card--back .brand-tagline { margin-top: 4px; }

  .contacts {
    position: absolute; left: 40px; bottom: 34px;
    display: grid; grid-template-columns: 16px auto; row-gap: 2px;
    font-size: 14px; line-height: 1.35;
  }
  .contacts dt { color: var(--orange); font-weight: 400; }
  .contacts dd { color: var(--ink); white-space: nowrap; }

  .address {
    position: absolute; left: 292px; top: 150px;
    padding-left: 14px; border-left: 1.5px solid var(--orange);
    font-size: 11.5px; line-height: 1.5; font-style: normal; color: var(--ink);
    white-space: nowrap;
  }
</style>
</head>
<body>
<main class="canvas">
  <section class="card card--front" aria-label="Card front">
    <div class="brand-mark"></div>
    <div class="brand">
      <div class="brand-name">torvalo</div>
      <div class="brand-tagline">Precision Packaging</div>
    </div>
  </section>

  <section class="card card--back" aria-label="Card back">
    <div class="brand">
      <div class="brand-mark"></div>
      <div>
        <div class="brand-name">torvalo</div>
        <div class="brand-tagline">Precision Packaging</div>
      </div>
    </div>

    <dl class="contacts">
      <dt>T</dt><dd>22 418 6093</dd>
      <dt>M</dt><dd>91 326 7041</dd>
      <dt>F</dt><dd>22 418 6135</dd>
      <dt>E</dt><dd>torvalo.ac@correiomx.com</dd>
    </dl>

    <address class="address">
      SEDE &amp; ARMAZÉM<br>
      Rua Das Figueiras do Monte, 312<br>
      Valmora 4520-832 Valmora - VN Teixal<br>
      Portugal
    </address>
  </section>
</main>
</body>
</html>
```